Display Banners for trade show 33" wide x 80" wide

We are a software development company and we have a new product we are calling "Velto". Which stands for Vendor Enabled Layout Tracking Organizer. Velto will become an app that building product sales people will use from when a client walks into the showroom all through the design process to the close of the sale. We are going to a trade show and need graphics for the 2 pull up banners that will be part of our display. I will attach some ideas we started playing with. We really need a Velto Logo plus the banner art.

Target Market(s)

Manufacturers of building products

Industry/Entity Type

It Company

Font styles to use
Serif

Requirements
Nice to have
• We want to tell the story of a total solution all in one product. We want the sales designer to never put down their tablet from start to finish. We want to stress the "cloud-based" aspect of the program. the banners are a backdrop to set the mood for Velto - mysterious, in the clouds, etc.

```html
<!DOCTYPE html>
<html lang="en">
<head>
<meta charset="utf-8">
<title>Velto – Trade Show Banner</title>
<link rel="stylesheet" href="https://fonts.googleapis.com/css2?family=Saira:wght@200;300;500&display=swap">
<style>
  :root {
    --edge-grey: #d9d9d9;
    --paper: #ffffff;
    --ink-blue: #1b5f86;
    --ink-grey: #5a6670;
    --panel-light: #1d76a3;
    --panel-mid: #0f4a70;
    --panel-dark: #0a3050;
    --line-white: #ffffff;
  }
  * { margin: 0; padding: 0; box-sizing: border-box; }
  html, body { width: 1200px; height: 2904px; overflow: hidden; background: var(--edge-grey); }
  .banner { display: block; width: 1200px; height: 2904px; }
  .brand-name { font-family: "Saira", sans-serif; font-weight: 500; fill: var(--ink-blue); letter-spacing: 10px; }
  .brand-tagline { font-family: "Saira", sans-serif; font-weight: 300; fill: var(--ink-grey); }
  .acronym-word { font-family: "Saira", sans-serif; font-weight: 200; fill: var(--line-white); }
  .connector { fill: none; stroke: var(--line-white); stroke-width: 4; }
  .connector-dot { fill: var(--line-white); }
  .icon-stroke { fill: none; stroke: var(--line-white); stroke-width: 12; stroke-linejoin: round; }
  .icon-fill { fill: var(--line-white); }
</style>
</head>
<body>
<svg class="banner" viewBox="0 0 1200 2904" xmlns="http://www.w3.org/2000/svg" role="img" aria-label="Velto banner: Vendor Enabled Layout Tracking Organizer">
  <defs>
    <radialGradient id="panel-glow" cx="600" cy="1950" r="1500" gradientUnits="userSpaceOnUse">
      <stop offset="0" stop-color="var(--panel-light)"/>
      <stop offset="0.5" stop-color="var(--panel-mid)"/>
      <stop offset="1" stop-color="var(--panel-dark)"/>
    </radialGradient>
  </defs>

  <!-- header band -->
  <rect class="header-band" x="0" y="24" width="1200" height="536" fill="var(--paper)"/>

  <!-- brand name -->
  <text class="brand-name" x="600" y="490" font-size="150" text-anchor="middle">VELTO</text>
  <text class="brand-tagline" x="600" y="542" font-size="24" text-anchor="middle" textLength="720" lengthAdjust="spacing">VENDOR ENABLED LAYOUT TRACKING ORGANIZER</text>

  <!-- main panel -->
  <rect class="main-panel" x="0" y="560" width="1200" height="2320" fill="url(#panel-glow)"/>

  <!-- acronym connectors -->
  <g class="acronym-connectors">
    <polyline class="connector" points="540,580 540,605 220,605 220,870 236,870"/>
    <polyline class="connector" points="420,580 420,630 160,630 160,1050 236,1050"/>
    <polyline class="connector" points="300,580 300,655 100,655 100,1205 236,1205"/>
    <polyline class="connector" points="700,580 700,605 1070,605 1070,1330 1032,1330"/>
    <polyline class="connector" points="840,580 840,630 1110,630 1110,1444 1072,1444"/>
    <circle class="connector-dot" cx="540" cy="580" r="7"/>
    <circle class="connector-dot" cx="420" cy="580" r="7"/>
    <circle class="connector-dot" cx="300" cy="580" r="7"/>
    <circle class="connector-dot" cx="700" cy="580" r="7"/>
    <circle class="connector-dot" cx="840" cy="580" r="7"/>
  </g>

  <!-- acronym words -->
  <g class="acronym-words">
    <text class="acronym-word" x="248" y="960" font-size="256" textLength="712" lengthAdjust="spacingAndGlyphs">VENDOR</text>
    <text class="acronym-word" x="248" y="1120" font-size="200" textLength="712" lengthAdjust="spacingAndGlyphs">ENABLED</text>
    <text class="acronym-word" x="248" y="1272" font-size="188" textLength="724" lengthAdjust="spacingAndGlyphs">LAYOUT</text>
    <text class="acronym-word" x="248" y="1380" font-size="143" textLength="772" lengthAdjust="spacingAndGlyphs">TRACKING</text>
    <text class="acronym-word" x="248" y="1500" font-size="160" textLength="812" lengthAdjust="spacingAndGlyphs">ORGANIZER</text>
  </g>

  <!-- cloud icon -->
  <path class="icon-stroke cloud-icon" d="M470,1790 C420,1790 410,1720 460,1705 C455,1655 520,1640 545,1670 C565,1615 660,1610 680,1670 C740,1650 790,1700 770,1745 C810,1760 800,1790 760,1790 Z"/>

  <!-- cloud-to-device link -->
  <polyline class="connector" points="420,1712 180,1712 180,2312 260,2312"/>
  <circle class="connector-dot" cx="180" cy="2312" r="12"/>

  <!-- monitor icon -->
  <g class="monitor-icon">
    <rect class="icon-stroke" x="266" y="2086" width="668" height="446" rx="20"/>
    <rect class="icon-fill" x="260" y="2480" width="680" height="58" rx="10"/>
    <path class="icon-fill" d="M540,2538 L660,2538 L680,2690 L520,2690 Z"/>
    <rect class="icon-fill" x="450" y="2680" width="300" height="34" rx="8"/>
  </g>
</svg>
</body>
</html>
```